Flyer-Design für Hausarztpraxis
Zielgruppe
Hausarztpraxis, Zielgruppe junge Patienten ...
Aufgabenstellung
Mein aktueller Flyer sollte modernisiert werden ... Texte können gern überarbeitet werden... Neue Fotos der Praxis werden noch gemacht. DH die Datei sollte so sein, dass ich die Fotos anpassen kann hinterher
Farbe gern in dem schönen Magenta wie das Logo
Aufbau des Flysers sollte ebenfalls optimiert werden.

```html
<!DOCTYPE html>
<html lang="de">
<head>
<meta charset="utf-8">
<title>Flyer Hausarztpraxis – Innenseite</title>
<link href="https://fonts.googleapis.com/css2?family=Open+Sans:wght@400;600;700;800&display=swap" rel="stylesheet">
<style>
  :root {
    --magenta: #cf2b4b;
    --magenta-dark: #b92140;
    --ink: #2e2e30;
    --paper: #f6f5f2;
    --stage: #d9d5cf;
    --photo-light: #dcdad5;
    --photo-mid: #b9b6b0;
  }
  * { box-sizing: border-box; margin: 0; padding: 0; }
  html, body { width: 1200px; height: 960px; overflow: hidden; }
  body {
    background: var(--stage);
    font-family: "Open Sans", Arial, sans-serif;
    color: var(--ink);
    position: relative;
  }
  .flyer {
    position: absolute; left: 30px; top: 77px;
    width: 1140px; height: 806px;
    display: flex;
    box-shadow: 0 10px 30px rgba(0,0,0,.15);
  }
  .panel {
    position: relative; width: 380px; height: 806px;
    background: var(--paper); overflow: hidden;
  }
  .panel + .panel { border-left: 1px solid #e4e2dd; }
  .panel svg.shape { position: absolute; left: 0; top: 0; }
  .content { position: absolute; left: 34px; right: 30px; }
  h1.headline {
    color: var(--magenta); font-weight: 800; font-size: 23px;
    line-height: 1.05; text-transform: uppercase;
  }
  h2.section {
    color: var(--magenta); font-weight: 700; font-size: 17px;
    margin: 14px 0 5px;
  }
  p { font-size: 12px; line-height: 1.45; margin-bottom: 8px; }
  p.greeting { font-weight: 700; margin-top: 10px; }
  .hours { font-weight: 700; font-size: 16.5px; line-height: 1.25; margin-bottom: 8px; }
  .photo-frame {
    position: absolute; left: 18px; top: 368px; width: 330px; height: 438px;
    border: 2px solid #3a3a3a; border-bottom: none;
  }
  .speech {
    position: absolute; left: 196px; top: 516px; width: 190px; height: 150px;
  }
  .speech-text {
    position: absolute; left: 218px; top: 548px; width: 146px;
    color: var(--magenta); font-weight: 700; font-size: 11.5px;
    line-height: 1.28; text-align: center; margin: 0;
  }
  .brand {
    position: absolute; left: 0; right: 0; top: 662px;
    color: #fff; text-align: center;
  }
  .brand-mark {
    width: 42px; height: 42px; border-radius: 50%;
    border: 3px solid #fff; margin: 0 auto 10px;
  }
  .brand-kicker { font-size: 10px; letter-spacing: 4px; text-transform: uppercase; }
  .brand-name { font-size: 19px; font-weight: 600; letter-spacing: 1px; margin: 2px 0 3px; }
  .brand-tagline { font-size: 8px; letter-spacing: 2.5px; text-transform: uppercase; }
  .brand-rule { width: 280px; height: 1px; background: #fff; margin: 4px auto; opacity: .8; }
</style>
</head>
<body>
<main class="flyer">

  <section class="panel panel-intro">
    <svg class="shape" width="380" height="806" viewBox="0 0 380 806">
      <defs>
        <linearGradient id="phoneTone" x1="0" y1="0" x2="1" y2="1">
          <stop offset="0" stop-color="#e6e4df"/>
          <stop offset="1" stop-color="#b6b3ad"/>
        </linearGradient>
      </defs>
      <path role="img" aria-label="Foto: alter Telefonhörer mit Kabel auf hellem Grund"
            d="M0 0 H380 V110 Q190 155 0 215 Z" fill="url(#phoneTone)"/>
      <path d="M0 772 Q200 792 380 806 H0 Z" fill="var(--magenta)"/>
    </svg>
    <div class="content" style="top:176px;">
      <h1 class="headline">Alle Neuerungen auf<br>einen Blick</h1>
      <p class="greeting">Liebe Patientinnen und Patienten,</p>
      <p>Zum 1. Oktober habe ich nach fast zwei Jahren intensiver Einarbeitung die Praxis von Herrn Dr. Brandauer übernommen.</p>
      <p>In diesem Flyer sehen sie all unsere Neuerungen rund um die Praxis.</p>
      <h2 class="section">Sprechstunden</h2>
      <p>Eine unserer sicher für Sie entscheidensten Veränderung sind unsere neuen Praxisöffnungszeiten.</p>
      <div class="hours">Mo 8-11:30 sowie 14-17 Uhr<br>Die 8-13 Uhr / Mi 8-13 Uhr<br>Do 8-11:30 sowie 14-18 Uhr<br>Fr 8-11:30</div>
      <p>Telefonisch erreichen Sie uns täglich von 8:30-11:00 Uhr sowie Montags und Donnerstags von 14:00-16:00 Uhr.</p>
      <h2 class="section">Laborzeiten</h2>
      <p>Unsere Laborzeiten sind nun vor der eigentlichen Sprechstunde von 7:15 -8:00 Uhr. Dazu kommt, dass Sie inzwischen die Möglichkeit haben, auch über unsere Website www.hausarzt-lindenau.de, <strong>online Termine</strong> zu vereinbaren.</p>
    </div>
  </section>

  <section class="panel panel-photo">
    <svg class="shape" width="380" height="806" viewBox="0 0 380 806">
      <defs>
        <linearGradient id="roomTone" x1="0" y1="0" x2="1" y2="1">
          <stop offset="0" stop-color="#f0efec"/>
          <stop offset=".6" stop-color="var(--photo-light)"/>
          <stop offset="1" stop-color="#5a5a5a"/>
        </linearGradient>
      </defs>
      <path d="M0 0 H380 V26 Q190 12 0 0 Z" fill="var(--magenta)"/>
      <rect role="img" aria-label="Foto: Behandlungszimmer mit Liege vor einem Fenster mit Jalousie"
            x="0" y="380" width="380" height="426" fill="url(#roomTone)"/>
    </svg>
    <div class="content" style="top:50px;">
      <h2 class="section">Rezepte</h2>
      <p>Rezepte sollten ein Tag vor Abholung auf unsere Rezepthotline gesprochen werden, oder in den neuen Briefkasten im Hausflur eingeworfen werden. Diese werden dann nach der Sprechzeit für sie fertig-gestellt</p>
    </div>
    <div class="photo-frame"></div>
    <svg class="speech" viewBox="0 0 190 150">
      <path d="M20 20 Q95 -10 170 30 Q195 70 165 110 Q120 140 55 128 L28 145 L36 120 Q0 95 6 60 Q8 35 20 20 Z"
            fill="#f6f5f2" stroke="var(--magenta)" stroke-width="3"/>
    </svg>
    <p class="speech-text">Ich werde Sie mit Leidenschaft medizinisch betreuen und auch mit Herz für Ihre Probleme da sein!</p>
  </section>

  <section class="panel panel-services">
    <svg class="shape" width="380" height="806" viewBox="0 0 380 806">
      <path d="M0 640 Q190 624 380 606 V806 H0 Z" fill="var(--magenta)"/>
    </svg>
    <div class="content" style="top:30px;">
      <h2 class="section">Neue Praxissoftware</h2>
      <p>Wie Sie vielleicht feststellen konnten haben wir eine neue Praxissoftware und Hardware, um die Praxisabläufe zu optimieren und Ihnen kürzere Wartezeiten anbieten zu können. Über unseren TV im Wartezimmer sehen sie immer alle Neuigkeiten, wie Urlaube oder Kurse.</p>
      <h2 class="section">Ultraschalluntersuchungen</h2>
      <p>Inzwischen können wir auch Ultraschallunterschungen der Schilddrüse, des Bauches sowie der Gefäße nach Leitlinie Stufe 2 anbieten.</p>
      <h2 class="section">Check-Ups</h2>
      <p>Es besteht auch die Möglichkeit außerhalb der kassenärztlichen Leistungen Check-UPs wahrzunehmen, wenn Sie es wünschen! Zum Beispiel ein erweiterter Frauen oder Männer Check.</p>
      <h2 class="section">Hyaloronsäure-Filler</h2>
      <p>Im Bereich der Ästhetik bieten wir Ihnen Hyaloronsäure-Filler im Gesicht zur Faltenenminimierung an.</p>
      <h2 class="section">Autogenes Training</h2>
      <p>Ebenfalls neu bieten wir Ihnen die Möglichkeit eine Anleitung für autogenes Training zu erhalten.</p>
    </div>
    <div class="brand">
      <div class="brand-mark"></div>
      <div class="brand-kicker">Hausarztpraxis</div>
      <div class="brand-rule"></div>
      <div class="brand-name">DR. MED. MARLENE HOFSTETTER</div>
      <div class="brand-rule"></div>
      <div class="brand-tagline">Weil wir lieben, was wir machen</div>
    </div>
  </section>

</main>
</body>
</html>
```